Bully breed rescue website

I need a website for my bully breed rescue. We rescue bully breeds from up and down the east coast of the United States and train them as service dogs for people with limited mobility disabilities. I don't want a lot of white space. I want it to be modern and slick and colorful and still look professional. I want it to be different and have a lot of wow factor. I linked a copy of my logo.

Number of Pages Required

5+ page

Font styles to use
Sans Serif

Colors

Designer to choose colors to be used in the design.

Requirements
Must have
• Moving aspects. Blog and ecommerce.
• 1.) Home page
• 2.) Services- something modular
• 3.) About US
• 4.) Blog
• 5.) Application page
• 6.) Donation page
• 7.) Contact Us
Nice to have
• Large Slider of photos on home page
• vertical menu bar
Should not have
• Lots of white space. Dont want it to look like a template or any other site

```html
<!DOCTYPE html>
<html lang="en">
<head>
<meta charset="utf-8">
<title>Bully Haven – Save a Bully</title>
<link href="https://fonts.googleapis.com/css2?family=Nunito:wght@400;600;700;800&family=Playball&family=Libre+Baskerville:wght@400;700&family=Kalam:wght@700&display=swap" rel="stylesheet">
<style>
:root{
  --orange:#f7a81e;
  --orange-deep:#f39a12;
  --orange-light:#fbc048;
  --yellow-soft:#f6ecc8;
  --red:#e8242f;
  --ink:#2b2b2b;
  --grey:#777;
  --light:#f7f7f7;
  --white:#fff;
  --card-grey:#d8cfcf;
}
*{box-sizing:border-box;margin:0;padding:0}
html,body{width:1200px;height:2711px;overflow:hidden}
body{position:relative;font-family:'Nunito',sans-serif;color:var(--ink);background:var(--white)}
.abs{position:absolute}

/* hero */
.hero{position:absolute;left:0;top:0;width:1200px;height:1308px;background:linear-gradient(160deg,var(--orange-light) 0%,var(--orange) 45%,var(--orange-deep) 100%);overflow:hidden}
.hero-facets{position:absolute;inset:0}
.brand{position:absolute;left:166px;top:0;width:277px;height:166px;z-index:2}
.brand-name{position:absolute;left:0;top:52px;width:277px;text-align:center;font-weight:800;font-size:19px;color:var(--ink)}
.brand-dot{position:absolute;left:126px;top:18px;width:24px;height:24px;border-radius:50%;background:var(--ink)}
.top-contact{position:absolute;right:128px;top:22px;display:flex;align-items:center;gap:22px;font-size:14px;color:var(--white);white-space:nowrap;z-index:3}
.top-contact span{display:flex;align-items:center;gap:8px}
.menu-btn{position:absolute;left:1086px;top:16px;width:105px;height:33px;background:var(--white);border-radius:2px;display:flex;align-items:center;justify-content:center;gap:10px;font-weight:800;font-size:16px;z-index:4}
.menu-list{position:absolute;left:1058px;top:60px;width:136px;height:269px;background:var(--white);box-shadow:0 3px 10px rgba(0,0,0,.15);list-style:none;padding:12px 10px;z-index:4}
.menu-list li{font-weight:800;font-size:15px;line-height:34px;color:var(--ink);white-space:nowrap}
.menu-list li.current{color:#bbb;font-weight:600}
.slide-dots{position:absolute;left:1143px;top:328px;z-index:3}
.slide-dots span{display:block;width:12px;height:12px;border-radius:50%;background:rgba(255,255,255,.55);margin-bottom:14px}
.hero-photo{position:absolute;left:470px;top:117px;width:687px;height:515px;border-radius:200px 200px 20px 20px;background:radial-gradient(ellipse at 60% 55%,#f4f0ea 0%,#cfc6bc 45%,rgba(60,55,50,.55) 100%);z-index:1}
.hero-title{position:absolute;left:155px;top:228px;font-family:'Playball',cursive;font-size:100px;font-weight:400;color:var(--white);line-height:1;z-index:2}
.hero-text{position:absolute;left:157px;top:356px;width:490px;font-family:'Libre Baskerville',serif;font-weight:700;font-size:18.5px;line-height:29px;color:var(--ink);z-index:2}
.hero-highlight{position:absolute;left:155px;top:454px;font-family:'Libre Baskerville',serif;font-size:24px;color:var(--white);letter-spacing:.5px;white-space:nowrap;z-index:2}
.btn{position:absolute;display:flex;align-items:center;justify-content:center;font-weight:800;font-size:13px;text-transform:uppercase;letter-spacing:.5px;white-space:nowrap}
.btn-donate{left:150px;top:520px;width:121px;height:29px;background:var(--red);color:var(--white);z-index:2}
.btn-contact{left:276px;top:520px;width:122px;height:29px;background:var(--white);color:var(--ink);z-index:2}

/* mission cards */
.mission{position:absolute;left:186px;top:797px;width:808px;height:341px;display:flex;box-shadow:0 4px 14px rgba(0,0,0,.12)}
.mission-card{width:280px;height:341px;background:var(--white);position:relative}
.mission-card.first{width:248px}
.mission-card.alt{background:var(--card-grey)}
.mission-photo{position:absolute;left:30px;top:55px;right:30px;height:200px;border-radius:8px}
.mission-card.alt .mission-photo{left:0;right:0;top:0;height:255px;border-radius:0}
.mission-caption{position:absolute;left:0;right:0;top:267px;text-align:center;font-family:'Libre Baskerville',serif;font-size:13px;line-height:22px;text-transform:uppercase;color:var(--ink);white-space:nowrap}
.mission-tab{position:absolute;top:-50px;width:110px;height:60px}
.btn-videos{left:453px;top:1193px;width:293px;height:61px;background:var(--red);color:var(--white);font-size:22px;font-weight:700;letter-spacing:1px;box-shadow:0 4px 10px rgba(0,0,0,.2)}

/* work */
.work{position:absolute;left:0;top:1308px;width:1200px;height:963px;background:var(--light);overflow:hidden}
.section-title{position:absolute;font-family:'Kalam',cursive;font-weight:700;font-size:48px;color:var(--ink);line-height:1;white-space:nowrap}
.work-sub{position:absolute;left:380px;top:107px;width:440px;text-align:center;font-size:14px;line-height:19px;color:#444}
.work-photo{position:absolute;top:201px;height:246px;border:5px solid var(--white);box-shadow:0 2px 6px rgba(0,0,0,.1)}
.slider-arrow{position:absolute;top:295px;width:50px;height:50px;background:var(--white);border:1px solid #e3d9b9;display:flex;align-items:center;justify-content:center}

.contact-sub{position:absolute;left:181px;top:588px;font-size:14px;color:#444}
.form-box{position:absolute;left:173px;top:644px;width:416px;height:198px;background:var(--white);box-shadow:0 3px 14px rgba(0,0,0,.15)}
.form-title{position:absolute;left:27px;top:28px;font-size:20px;color:var(--red);font-weight:600}
.form-input{position:absolute;left:27px;top:79px;width:362px;height:38px;border:1px solid #ccc;font-size:12px;color:#999;display:flex;align-items:center;padding-left:16px}
.form-input svg{position:absolute;right:12px;top:11px}
.btn-next{left:219px;top:131px;width:170px;height:37px;background:var(--red);color:var(--white);font-size:13px;text-transform:none;font-weight:600}

.post{position:absolute;left:611px;width:430px;height:92px}
.post-thumb{position:absolute;left:0;top:0;width:86px;height:91px}
.post-text{position:absolute;left:105px;top:8px;width:320px;font-size:13px;line-height:20px;color:var(--red)}
.post-meta{position:absolute;left:105px;top:76px;font-size:11px;color:var(--grey);white-space:nowrap}
.post-meta span{margin-left:26px}

/* map */
.map{position:absolute;left:0;top:2271px;width:1200px;height:259px;background:linear-gradient(180deg,#eceee6,#e4e7dc)}
.map-pin{position:absolute;left:747px;top:2343px}

/* footer */
.footer-links{position:absolute;left:172px;top:2583px;width:270px;font-size:12px;line-height:18px;color:var(--ink)}
.footer-copy{position:absolute;left:172px;top:2630px;font-size:12px;color:var(--ink)}
.accept-title{position:absolute;left:716px;top:2556px;font-family:'Kalam',cursive;font-weight:700;font-size:30px}
.payments{position:absolute;left:716px;top:2608px;display:flex;gap:22px;font-weight:800;font-size:14px;color:#9a9a9a;white-space:nowrap}
.socials{position:absolute;left:722px;top:2658px;display:flex;gap:12px}
.socials span{width:10px;height:10px;border-radius:50%;background:#888}
</style>
</head>
<body>

<header class="hero">
  <svg class="hero-facets" width="1200" height="1308" viewBox="0 0 1200 1308">
    <polygon points="0,0 420,0 160,700 0,520" fill="#fbbb3e" opacity=".55"/>
    <polygon points="0,1000 1200,1308 0,1308" fill="#f59a12" opacity=".6"/>
    <polygon points="640,760 1200,520 1200,1308" fill="#fbbf4d" opacity=".45"/>
    <polygon points="300,430 820,640 560,1020" fill="#fcc957" opacity=".35"/>
  </svg>

  <div class="brand">
    <svg width="277" height="166" viewBox="0 0 277 166"><polygon points="0,0 277,0 138.5,166" fill="#fff"/><polygon points="6,0 271,0 138.5,156" fill="none" stroke="#ddd" stroke-width="2"/></svg>
    <span class="brand-dot"></span>
    <div class="brand-name">Bully Haven</div>
  </div>

  <div class="top-contact">
    <span>
      <svg width="16" height="16" viewBox="0 0 16 16"><rect width="16" height="16" rx="2" fill="#fff"/><path d="M5 3.5l2 2-1.2 1.4a7 7 0 0 0 3.3 3.3L10.5 9l2 2-1.5 1.5C7.5 12.5 3.5 8.5 3.5 5z" fill="#f7a81e"/></svg>
      +01 555 014 282
    </span>
    <span>
      <svg width="20" height="15" viewBox="0 0 20 15"><rect width="20" height="15" rx="1" fill="#fff"/><path d="M1 1l9 7 9-7" fill="none" stroke="#f7a81e" stroke-width="1.6"/></svg>
      info@bullyhaven.org
    </span>
  </div>
  <div class="menu-btn">
    <svg width="15" height="12" viewBox="0 0 15 12"><rect width="15" height="2" fill="#2b2b2b"/><rect y="5" width="15" height="2" fill="#2b2b2b"/><rect y="10" width="15" height="2" fill="#2b2b2b"/></svg>
    MENU
  </div>
  <ul class="menu-list">
    <li class="current">HOME</li><li>SERVICES</li><li>ABOUT US</li><li>BLOG</li><li>APPLICATION</li><li>DONATION</li><li>CONTACT US</li>
  </ul>
  <div class="slide-dots"><span></span><span></span><span></span></div>

  <div class="hero-photo" role="img" aria-label="Photo of a trainer kneeling with two white and black bully dogs"></div>

  <h1 class="hero-title">Save a Bully</h1>
  <p class="hero-text">We rescue bully breeds from the east coast of the United States and train them as service dogs for people with</p>
  <p class="hero-highlight">LIMITED MOBILITY DISABILITIES.</p>
  <div class="btn btn-donate">Donate Now</div>
  <div class="btn btn-contact">Contact Us</div>

  <section class="mission">
    <div class="mission-card first">
      <svg class="mission-tab" style="left:69px" viewBox="0 0 110 60"><polygon points="0,50 30,0 80,0 110,50 110,60 0,60" fill="#fff"/><circle cx="55" cy="26" r="9" fill="#2b2b2b"/><rect x="40" y="42" width="30" height="2" fill="#2b2b2b"/><rect x="45" y="48" width="20" height="2" fill="#2b2b2b"/></svg>
      <div class="mission-photo" role="img" aria-label="Photo of a brown pit bull sitting" style="background:radial-gradient(circle at 50% 50%,#c0875a 0%,#e8d6c6 55%,#fff 80%)"></div>
      <p class="mission-caption">We rescue<br>bully breeds</p>
    </div>
    <div class="mission-card alt">
      <svg class="mission-tab" style="left:85px" viewBox="0 0 110 60"><polygon points="0,50 30,0 80,0 110,50 110,60 0,60" fill="#fff"/><circle cx="55" cy="26" r="11" fill="none" stroke="#2b2b2b" stroke-width="3"/><circle cx="55" cy="26" r="4" fill="#2b2b2b"/><rect x="40" y="42" width="30" height="2" fill="#2b2b2b"/><rect x="45" y="48" width="20" height="2" fill="#2b2b2b"/></svg>
      <div class="mission-photo" role="img" aria-label="Photo of a dog walking beside a trainer on a leash" style="background:linear-gradient(90deg,#d8cfcf 0%,#b9a89c 45%,#7d6a60 60%,#3a4358 80%,#d8cfcf 100%)"></div>
      <p class="mission-caption">Train them as<br>service dogs</p>
    </div>
    <div class="mission-card">
      <svg class="mission-tab" style="left:85px" viewBox="0 0 110 60"><polygon points="0,50 30,0 80,0 110,50 110,60 0,60" fill="#fff"/><circle cx="52" cy="12" r="3.5" fill="#2b2b2b"/><path d="M52 17v10h9l4 8" fill="none" stroke="#2b2b2b" stroke-width="3"/><circle cx="52" cy="30" r="7" fill="none" stroke="#2b2b2b" stroke-width="2.5"/><rect x="40" y="42" width="30" height="2" fill="#2b2b2b"/><rect x="45" y="48" width="20" height="2" fill="#2b2b2b"/></svg>
      <div class="mission-photo" role="img" aria-label="Photo of a man in a wheelchair with his service dog" style="left:20px;right:10px;background:radial-gradient(circle at 55% 55%,#55657e 0%,#a4a7b0 45%,#fff 80%)"></div>
      <p class="mission-caption">Use them for people with<br>limited mobility disabilities</p>
    </div>
  </section>

  <div class="btn btn-videos">VIEW OUR VIDEOS</div>
</header>

<section class="work">
  <svg class="abs" style="left:0;top:0" width="1200" height="963" viewBox="0 0 1200 963">
    <polygon points="0,0 330,0 0,230" fill="var(--yellow-soft)" opacity=".8"/>
    <polygon points="0,300 120,380 0,450" fill="var(--yellow-soft)" opacity=".8"/>
    <polygon points="930,420 1200,300 1200,963 860,963" fill="var(--yellow-soft)" opacity=".7"/>
  </svg>
  <h2 class="section-title" style="left:506px;top:46px">Our Work</h2>
  <p class="work-sub">We have rescued and trained 1200 Bully Dogs and connected them with people with limited mobility disabilities</p>

  <div class="slider-arrow" style="left:51px"><svg width="12" height="20" viewBox="0 0 12 20"><path d="M10 2L2 10l8 8" fill="none" stroke="#999" stroke-width="2"/></svg></div>
  <div class="work-photo" style="left:175px;width:264px;background:linear-gradient(180deg,#3d6b2c 0%,#8a6448 50%,#5e8a3a 100%)" role="img" aria-label="Photo of a muscular brown bully dog standing on grass"></div>
  <div class="work-photo" style="left:471px;width:263px;background:linear-gradient(180deg,#7f9a5e 0%,#b55a4a 55%,#6a8a4a 100%)" role="img" aria-label="Photo of a trainer in a bite suit working with a dog"></div>
  <div class="work-photo" style="left:761px;width:262px;background:linear-gradient(180deg,#b34a3a 0%,#e592b6 45%,#8a7a5a 75%,#4f7a3a 100%)" role="img" aria-label="Photo of a smiling woman sitting on grass with two pit bulls"></div>
  <div class="slider-arrow" style="left:1097px"><svg width="12" height="20" viewBox="0 0 12 20"><path d="M2 2l8 8-8 8" fill="none" stroke="#999" stroke-width="2"/></svg></div>

  <h2 class="section-title" style="left:173px;top:532px">Contact Us</h2>
  <p class="contact-sub">For rescue, adoption and donation</p>
  <div class="form-box">
    <p class="form-title">Please Fill up the Form</p>
    <div class="form-input">Enter Your Name...
      <svg width="14" height="15" viewBox="0 0 14 15"><circle cx="7" cy="4" r="3.6" fill="#333"/><path d="M0 15c0-4.5 3-6.5 7-6.5s7 2 7 6.5z" fill="#333"/></svg>
    </div>
    <div class="btn btn-next">Next Step&nbsp;›</div>
  </div>

  <h2 class="section-title" style="left:611px;top:540px;font-size:36px">Recent Posts</h2>
  <article class="post" style="top:609px">
    <div class="post-thumb" role="img" aria-label="Photo of a grey pit bull wearing an orange bandana" style="background:linear-gradient(160deg,#6f8a5a,#8a8f96 50%,#e07a2a)"></div>
    <p class="post-text">Duis aute irure dolor in reprehenderit in voluptate velit esse cillum dolore eu fugiat nulla pariatur excepteur sint occaecat</p>
    <p class="post-meta">Admin<span>21st May,2018</span></p>
  </article>
  <article class="post" style="top:712px">
    <div class="post-thumb" role="img" aria-label="Photo of a woman with a small pit bull outdoors" style="background:linear-gradient(160deg,#4f7a3a,#d98aa8 50%,#8a8a7a)"></div>
    <p class="post-text">Voluptate velit esse quam nihil molestiae consequatur cupidatat non proident, sunt in culpa qui officia deserunt mollit anim id est laborum</p>
    <p class="post-meta">Admin<span>21st May,2018</span></p>
  </article>
  <article class="post" style="top:817px">
    <div class="post-thumb" role="img" aria-label="Photo of a pit bull playing with a purple ball" style="background:linear-gradient(160deg,#5e8a3a,#8a8f96 45%,#6a4a9a)"></div>
    <p class="post-text">Quis autem vel eum iure reprehenderit qui in ea velit esse quam nihil molestiae consequatur vel illum qui dolorem eum fugiat quo voluptas</p>
    <p class="post-meta">Admin<span>21st May,2018</span></p>
  </article>
</section>

<div class="map" role="img" aria-label="Road map of the central United States with the rescue location marked"></div>
<svg class="map-pin" width="18" height="26" viewBox="0 0 18 26"><path d="M9 0a9 9 0 0 1 9 9c0 7-9 17-9 17S0 16 0 9a9 9 0 0 1 9-9z" fill="#e8242f"/><circle cx="9" cy="9" r="3.5" fill="#fff"/></svg>

<footer>
  <p class="footer-links">Home | About Us | Donation | Application | Blog<br>| Privacy Policy | Contact Us</p>
  <p class="footer-copy">©Copyright information here</p>
  <h3 class="accept-title">We Accept</h3>
  <div class="payments"><span>NorthCard</span><span>Orbit Pay</span><span>Lumen</span><span>Meridian</span><span>Sendly</span></div>
  <div class="socials"><span></span><span></span><span></span><span></span><span></span></div>
</footer>

</body>
</html>
```